Brindle and Fern LLC | Land Clearing, Landscaping & Dump Trailer Services

Project Description: Brindle and Fern LLC Website Design
The website will be published using squarespace
Objective:
Design a visually compelling and conversion-driven website for Brindle and Fern LLC, a land solutions business based in Pickens County, Georgia. The site will highlight the company’s professionalism, locally rooted service, and commitment to quality in land clearing, grading, and dump trailer services.
Pages & Features to Include:
1. Landing Page (Homepage)
- Clear tagline: Sculpting Land with Precision and Power
- Call-to-Action (CTA) buttons: “Get a Free Quote” and “View Services”
- Service highlights with icons or photos (e.g., grading, mulching, hauling)
- Customer testimonials
- Embedded contact form
- Local Reviews Maps integration showing service area
2. Services + Pricing Page
- Organized list of services under 3 categories:
- **Land Clearing & Grading**
- Forestry Mulching
- Gravel Driveway Repair
- Minimum Job Fee:
- Dump Trailer Services
- Trailer Rental (Daily):
- Junk Removal (Full Load)
- Material Delivery: $ + mileage
- Specialty Jobs
- Stump removal, light demolition
- Each service section includes short descriptions and photos
- Optional quote form at the bottom with “Request a Quote” CTA
Design Style:
- Clean, professional design using clean tones
- Fonts that balance industrial strength and local charm
- Mobile-optimized with fast loading speeds and easy navigation
- SEO-optimized for terms like *land clearing Pickens County*, *grading services North Georgia*, and *dump trailer rental Jasper GA*, etc...

```html
<!DOCTYPE html>
<html lang="en">
<head>
<meta charset="utf-8">
<title>Brindle and Fern LLC | Land Clearing, Grading &amp; Dump Trailer Services</title>
<link rel="stylesheet" href="https://fonts.googleapis.com/css2?family=Outfit:wght@400;500;600;700;800&display=swap">
<style>
:root{
  --ink:#111;
  --black:#000;
  --green:#3d8b2f;
  --card:#e9e9e9;
  --muted:#777;
  --light:#f4f5f7;
  --star:#f5b50a;
  --white:#fff;
}
*{box-sizing:border-box;margin:0;padding:0}
html,body{width:1200px;height:4313px;overflow:hidden}
body{font-family:"Outfit",sans-serif;color:var(--ink);background:var(--white);position:relative}
a{color:inherit;text-decoration:none}

/* top bar */
.topbar{position:absolute;top:0;left:0;width:1200px;height:34px;background:var(--black);color:#fff;font-size:10px}
.topbar .rating{position:absolute;left:199px;top:11px;display:flex;gap:6px;align-items:center}
.stars{color:var(--star);letter-spacing:1px}
.social-dot{width:10px;height:10px;border-radius:50%;background:#fff;position:absolute}

/* header */
.header{position:absolute;top:34px;left:0;width:1200px;height:80px;background:#fff;border-bottom:1px solid #eee}
.brand{position:absolute;left:199px;top:25px;display:flex;align-items:center;gap:8px;font-weight:800;font-size:18px;color:var(--ink)}
.brand .mark{width:30px;height:30px;background:var(--green);border-radius:4px}
.nav{position:absolute;right:199px;top:25px;display:flex;gap:22px;align-items:center;font-size:13px;font-weight:500}
.btn{display:inline-flex;align-items:center;justify-content:center;font-weight:600;border-radius:3px;font-size:11px}
.btn-green{background:var(--green);color:#fff}
.nav .btn{height:30px;padding:0 12px;font-size:10px}

/* hero */
.hero{position:absolute;top:114px;left:0;width:1200px;height:526px;overflow:hidden;
  background:linear-gradient(160deg,#5a6068 0%,#3a3d40 35%,#2a2b26 60%,#1e1f1a 100%)}
.hero .shade{position:absolute;right:-120px;top:-40px;width:700px;height:700px;border-radius:50%;background:radial-gradient(circle at 0 50%,transparent 60%,rgba(0,0,0,.35) 61%)}
.hero h1{position:absolute;left:199px;top:120px;color:#fff;font-size:46px;line-height:44px;font-weight:800}
.hero p{position:absolute;left:199px;top:235px;color:#fff;font-size:13px}
.hero .ctas{position:absolute;left:199px;top:275px;display:flex;gap:10px}
.hero .ctas .btn{height:30px;padding:0 20px;font-size:9px}
.btn-black{background:#000;color:#fff}
.btn-white{background:#fff;color:#000}

/* services */
.services{position:absolute;top:640px;left:0;width:1200px;height:1035px;background:#fafafa}
.chip{position:absolute;left:199px;top:38px;border:1px solid #ddd;border-radius:14px;padding:3px 10px;font-size:9px;background:#fff;display:flex;gap:5px;align-items:center}
.services h2{position:absolute;left:199px;top:78px;font-size:36px;font-weight:700}
.card{position:absolute;width:253px;height:197px;background:var(--card);border-radius:10px}
.card .photo{position:absolute;left:10px;top:10px;width:233px;height:93px;border-radius:4px}
.card .desc{position:absolute;left:16px;top:120px;width:190px;font-size:9px;color:var(--muted);line-height:14px}
.card .title{position:absolute;left:16px;top:167px;font-size:12px;font-weight:600}
.card .notch{position:absolute;right:0;bottom:0;width:56px;height:48px;background:#fafafa;border-top-left-radius:14px}
.card .arrow{position:absolute;right:10px;bottom:5px;width:38px;height:38px;border-radius:50%;background:var(--card);display:flex;align-items:center;justify-content:center}

/* about */
.about-box{position:absolute;left:199px;top:1726px;width:479px;height:263px;background:#000;border-radius:10px;color:#fff}
.about-box h2{position:absolute;left:30px;top:50px;font-size:23px;font-weight:600}
.about-box p{position:absolute;left:30px;top:92px;width:350px;font-size:9.5px;line-height:17.5px}
.about-photo{position:absolute;left:665px;top:1736px;width:321px;height:243px;border-radius:8px;background:linear-gradient(180deg,#4e5f3d 0%,#6e7a5c 40%,#b9b4a8 70%,#d9d6cf 100%)}

/* testimonials */
.testimonials{position:absolute;top:2037px;left:0;width:1200px;height:454px;background:var(--light);text-align:center}
.eyebrow{position:absolute;left:0;width:1200px;top:62px;font-size:8px;letter-spacing:3px;color:#555}
.testimonials h2{position:absolute;left:0;width:1200px;top:86px;font-size:18px;font-weight:600}
.testimonials .sub{position:absolute;left:0;width:1200px;top:117px;font-size:11px;color:#666}
.review{position:absolute;top:166px;width:253px;height:144px;background:#fff;border-radius:4px;text-align:left;padding:22px 22px}
.review p{font-size:9px;line-height:17px;color:#444}
.review .by{position:absolute;left:22px;bottom:26px;font-size:9px;display:flex;gap:6px;align-items:center}
.review .by .stars{color:#111;font-size:10px}
.review .by b{font-weight:600;letter-spacing:.5px}
.test-ctas{position:absolute;top:360px;left:0;width:1200px;display:flex;gap:10px;justify-content:center}
.test-ctas .btn{height:34px;padding:0 18px;font-size:10px}
.btn-outline{background:#fff;border:1px solid #333;color:#111;gap:6px}
.btn-outline i{width:9px;height:9px;border-radius:50%;border:2px solid #888;display:block}

/* quote band */
.quote-band{position:absolute;top:2491px;left:0;width:1200px;height:298px;background:#0d0d0d;color:#fff}
.quote-band blockquote{position:absolute;left:360px;top:60px;width:480px;font-size:18px;line-height:22.5px;font-weight:600}
.quote-band .who{position:absolute;left:360px;top:224px;font-size:11px;display:flex;gap:8px}
.quote-mark{position:absolute;right:10px;bottom:0;font-size:150px;line-height:110px;font-weight:800;color:#222;height:60px;overflow:hidden}

/* service area map */
.map{position:absolute;top:2789px;left:0;width:1200px;height:515px;background:linear-gradient(90deg,#e6ece2 0%,#e3e9de 45%,#9fd8ea 60%,#8fd3e8 100%)}
.map-tabs{position:absolute;left:0;top:6px;display:flex;background:#fff;font-size:10px;box-shadow:0 1px 3px rgba(0,0,0,.2)}
.map-tabs span{padding:6px 12px}
.map-tabs span:first-child{font-weight:600}
.areas-panel{position:absolute;left:733px;top:23px;width:268px;height:469px;background:#eef2f5;border-radius:6px;padding:14px}
.areas-panel h3{background:#fff;font-size:18px;font-weight:600;padding:14px 8px;border-radius:3px;margin-bottom:10px}
.areas-panel ul{list-style:none;height:368px;overflow:hidden;padding-right:10px;border-right:4px solid #d0d4d8}
.areas-panel li{background:#fff;font-size:10px;padding:12px 8px;margin-bottom:8px}
.areas-panel li b{font-weight:700}

/* cta */
.dark-base{position:absolute;top:3395px;left:0;width:1200px;height:918px;background:#000;border-radius:30px 30px 0 0}
.cta{position:absolute;top:3341px;left:199px;width:802px;height:375px;border-radius:14px;background:linear-gradient(180deg,#2a2d27 0%,#3c3b35 50%,#4a463e 100%)}
.cta h2{position:absolute;left:92px;top:90px;color:#fff;font-size:42px;line-height:45px;font-weight:800}
.cta p{position:absolute;left:92px;top:238px;width:320px;color:#ddd;font-size:10px;line-height:16px}
.cta .ctas{position:absolute;left:92px;top:286px;display:flex;gap:8px}
.cta .ctas .btn{height:26px;padding:0 10px;font-size:9px}
.btn-grey{background:#8b8b8b;color:#fff}

/* footer */
.footer{position:absolute;top:3860px;left:0;width:1200px;height:453px;color:#fff}
.footer .name{position:absolute;left:219px;top:7px;font-size:15px;font-weight:600}
.footer .fdot{left:223px;top:53px}
.footer .fbrand{position:absolute;left:223px;top:110px;display:flex;gap:8px;align-items:center;font-weight:700;font-size:14px;color:#555}
.footer .fbrand i{width:18px;height:18px;border:2px solid #555;display:block}
.fcol{position:absolute;top:10px;font-size:8px}
.fcol h4{font-size:8px;font-weight:600;margin-bottom:22px}
.fcol li{list-style:none;margin-bottom:16.5px;color:#eee}
.footer .rule{position:absolute;left:219px;top:395px;width:782px;height:1px;background:#222}
.footer .copy{position:absolute;left:219px;top:421px;font-size:7px;color:#aaa}
</style>
</head>
<body>

<div class="topbar">
  <div class="rating"><span class="stars">★★★★★</span><span>5 stars from Local Reviews</span></div>
  <span class="social-dot" style="left:988px;top:12px"></span>
</div>

<header class="header">
  <a class="brand" href="#"><span class="mark"></span>Brindle and Fern LLC</a>
  <nav class="nav">
    <a href="#">Services ⌄</a><a href="#">Projects</a><a href="#">Reviews</a><a href="#">About Us</a><a href="#">Contact</a>
    <a class="btn btn-green" href="#">Get a Free Quote</a>
  </nav>
</header>

<section class="hero" role="img" aria-label="Excavator and dump trailer on a cleared job site at dusk">
  <div class="shade"></div>
  <h1>Sculpting Land with<br>Precision and Power</h1>
  <p>Excellence in Excavation &amp; Grading Services</p>
  <div class="ctas"><a class="btn btn-black" href="#">Get a Free Quote</a><a class="btn btn-white" href="#">View Services</a></div>
</section>

<section class="services">
  <div class="chip"><svg width="9" height="9" viewBox="0 0 10 10"><circle cx="5" cy="5" r="4" fill="none" stroke="#333"/><path d="M3 5l1.5 1.5L7 3.5" fill="none" stroke="#333"/></svg>Services</div>
  <h2>Our Professional Services</h2>
</section>

<div class="card" style="left:199px;top:777px"><div class="photo" role="img" aria-label="Excavator digging a site" style="background:linear-gradient(180deg,#8a9aa8,#a68a62)"></div><p class="desc">Precise and reliable excavation and site preparation you can trust.</p><div class="title">Excavating</div><div class="notch"></div><div class="arrow"><svg width="10" height="10" viewBox="0 0 10 10"><path d="M2 8L8 2M3 2h5v5" fill="none" stroke="#111" stroke-width="1.3"/></svg></div></div>
<div class="card" style="left:474px;top:777px"><div class="photo" role="img" aria-label="Compact loader grading a yard" style="background:linear-gradient(180deg,#9fb0bd,#5d5646)"></div><p class="desc">Ensure precise, level groundwork for your perfect outdoor aesthetic.</p><div class="title">Grading</div><div class="notch"></div><div class="arrow"><svg width="10" height="10" viewBox="0 0 10 10"><path d="M2 8L8 2M3 2h5v5" fill="none" stroke="#111" stroke-width="1.3"/></svg></div></div>
<div class="card" style="left:748px;top:777px"><div class="photo" role="img" aria-label="Prepared gravel site" style="background:linear-gradient(180deg,#6e7478,#b9b9b6)"></div><p class="desc">Creating stable grounds for flawless landscape transformations.</p><div class="title">Site Preparation</div><div class="notch"></div><div class="arrow"><svg width="10" height="10" viewBox="0 0 10 10"><path d="M2 8L8 2M3 2h5v5" fill="none" stroke="#111" stroke-width="1.3"/></svg></div></div>

<div class="card" style="left:199px;top:998px"><div class="photo" role="img" aria-label="Overgrown land before clearing" style="background:linear-gradient(180deg,#8fa06a,#4a5a34)"></div><p class="desc">Efficient clearing solutions for your property's pristine transformation.</p><div class="title">Land Clearing</div><div class="notch"></div><div class="arrow"><svg width="10" height="10" viewBox="0 0 10 10"><path d="M2 8L8 2M3 2h5v5" fill="none" stroke="#111" stroke-width="1.3"/></svg></div></div>
<div class="card" style="left:474px;top:998px"><div class="photo" role="img" aria-label="Mower attachment cutting a field" style="background:linear-gradient(180deg,#6f9a4a,#3f6f2a)"></div><p class="desc">Efficient land clearing for overgrown areas, enhancing property appearance.</p><div class="title">Bush Hogging</div><div class="notch"></div><div class="arrow"><svg width="10" height="10" viewBox="0 0 10 10"><path d="M2 8L8 2M3 2h5v5" fill="none" stroke="#111" stroke-width="1.3"/></svg></div></div>
<div class="card" style="left:748px;top:998px"><div class="photo" role="img" aria-label="Fresh gravel driveway" style="background:linear-gradient(180deg,#7d8a6a,#a9a59a)"></div><p class="desc">Expertly crafted driveways for durability and aesthetic appeal.</p><div class="title">Gravel Driveways</div><div class="notch"></div><div class="arrow"><svg width="10" height="10" viewBox="0 0 10 10"><path d="M2 8L8 2M3 2h5v5" fill="none" stroke="#111" stroke-width="1.3"/></svg></div></div>

<div class="card" style="left:199px;top:1219px"><div class="photo" role="img" aria-label="Cleared house pad near a tree line" style="background:linear-gradient(180deg,#8fb7d8,#3d5a2c 45%,#c8a77a)"></div><p class="desc">Expertly prepare your land for a solid, level foundation.</p><div class="title">House Pads</div><div class="notch"></div><div class="arrow"><svg width="10" height="10" viewBox="0 0 10 10"><path d="M2 8L8 2M3 2h5v5" fill="none" stroke="#111" stroke-width="1.3"/></svg></div></div>
<div class="card" style="left:474px;top:1219px"><div class="photo" role="img" aria-label="Debris burn after a storm" style="background:linear-gradient(180deg,#7a7a78,#a8a49c)"></div><p class="desc">Swiftly restore your property with efficient post-storm debris removal.</p><div class="title">Storm Clean Up</div><div class="notch"></div><div class="arrow"><svg width="10" height="10" viewBox="0 0 10 10"><path d="M2 8L8 2M3 2h5v5" fill="none" stroke="#111" stroke-width="1.3"/></svg></div></div>
<div class="card" style="left:748px;top:1219px"><div class="photo" role="img" aria-label="Excavator bucket during demolition" style="background:linear-gradient(180deg,#5c8fd0,#9ab8da 60%,#8a7e6a)"></div><p class="desc">Seamlessly clear grounds for stunning and refreshed landscaping visions.</p><div class="title">Demolition</div><div class="notch"></div><div class="arrow"><svg width="10" height="10" viewBox="0 0 10 10"><path d="M2 8L8 2M3 2h5v5" fill="none" stroke="#111" stroke-width="1.3"/></svg></div></div>

<div class="card" style="left:199px;top:1440px"><div class="photo" role="img" aria-label="Mulching machine at sunset" style="background:linear-gradient(180deg,#d08a4a,#6a6a66 55%,#3b3f2c)"></div><p class="desc">Efficient land clearing with minimal disturbance for a healthier environment.</p><div class="title">Forestry Mulching</div><div class="notch"></div><div class="arrow"><svg width="10" height="10" viewBox="0 0 10 10"><path d="M2 8L8 2M3 2h5v5" fill="none" stroke="#111" stroke-width="1.3"/></svg></div></div>
<div class="card" style="left:474px;top:1440px"><div class="photo" role="img" aria-label="Cut tree stump on a lawn" style="background:linear-gradient(180deg,#4f7a34,#6b5a44 60%,#4a6a2e)"></div><p class="desc">Quick and efficient removal for a cleaner, safer landscape.</p><div class="title">Tree and Stump Removal</div><div class="notch"></div><div class="arrow"><svg width="10" height="10" viewBox="0 0 10 10"><path d="M2 8L8 2M3 2h5v5" fill="none" stroke="#111" stroke-width="1.3"/></svg></div></div>
<div class="card" style="left:748px;top:1440px"><div class="photo" role="img" aria-label="Dump trailer unloading gravel" style="background:linear-gradient(180deg,#4a78b8,#8aa6c8 50%,#9a9a98)"></div><p class="desc">Efficient, reliable dump trailer solutions for all your landscaping needs.</p><div class="title">Dump Trailer Services</div><div class="notch"></div><div class="arrow"><svg width="10" height="10" viewBox="0 0 10 10"><path d="M2 8L8 2M3 2h5v5" fill="none" stroke="#111" stroke-width="1.3"/></svg></div></div>

<div class="about-box">
  <h2>About Brindle and Fern LLC</h2>
  <p>Founded on dedication and integrity, Brindle and Fern LLC transforms landscapes with a passion for excellence. Our team unites experience with cutting-edge technology to deliver unparalleled land management. We value each client's vision, committing to honesty, reliability, and superior craftsmanship. Join our journey in crafting outdoor spaces that inspire and stand the test of time, rooted in our promise of outstanding service and community care.</p>
</div>
<div class="about-photo" role="img" aria-label="Work truck towing a compact tractor on a gravel lot"></div>

<section class="testimonials">
  <div class="eyebrow">TESTIMONIALS</div>
  <h2>Our clients love us</h2>
  <div class="sub">Here's some of what they had to say</div>
  <div class="review" style="left:199px"><p>Had my property leveled out and they did a fantastic job he was professional on time and took extra steps to make sure I was satisfied would highly recommend</p><div class="by"><span class="stars">★★★★★</span><i>by</i><b>COREY M.</b></div></div>
  <div class="review" style="left:474px"><p>Wade was great. He worked hard and his price was reasonable. We are very pleased. We recommend him.</p><div class="by"><span class="stars">★★★★★</span><i>by</i><b>DALE P.</b></div></div>
  <div class="review" style="left:748px"><p>Such a great guy love his work ethic and gets the job done for a great price!</p><div class="by"><span class="stars">★★★★★</span><i>by</i><b>HEATH R.</b></div></div>
  <div class="test-ctas"><a class="btn btn-green" href="#">See all reviews</a><a class="btn btn-outline" href="#"><i></i>Leave us a review</a></div>
</section>

<section class="quote-band">
  <blockquote>"If you ever need excavator services and or rip rap de-silt work, this is your guy. Wade at Brindle and Fern LLC Services is great with any construction equipment that needs to be operated for a vast amount of jobs at a fair price. I have worked with hundreds of vendors that do this type of work and he was not only pleasure to wor...</blockquote>
  <div class="who"><span class="stars">★★★★★</span><span>Marcus T.</span></div>
  <div class="quote-mark">”</div>
</section>

<section class="map" role="img" aria-label="Map of Pickens County, Georgia showing the service area">
  <div class="map-tabs"><span>Map</span><span>Satellite</span></div>
  <div class="areas-panel">
    <h3>We're here to help</h3>
    <ul>
      <li><b>01.</b> Pickens County, GA</li>
      <li><b>02.</b> Jasper, GA</li>
      <li><b>03.</b> Talking Rock, GA</li>
      <li><b>04.</b> Nelson, GA</li>
      <li><b>05.</b> Marble Hill, GA</li>
      <li><b>06.</b> Tate, GA</li>
      <li><b>07.</b> Big Canoe, GA</li>
      <li><b>08.</b> Ball Ground, GA</li>
    </ul>
  </div>
</section>

<div class="dark-base"></div>

<section class="cta" role="img" aria-label="Freshly cleared and graded land at dusk">
  <h2>Transform Your<br>Landscape<br>Today</h2>
  <p>Book our expert services for your land management needs and see immediate results. Act Now!</p>
  <div class="ctas"><a class="btn btn-green" href="#">Get a Free Quote</a><a class="btn btn-grey" href="#">View Services</a></div>
</section>

<footer class="footer">
  <div class="name">Brindle and Fern LLC</div>
  <span class="social-dot fdot"></span>
  <div class="fbrand"><i></i>Brindle and Fern LLC</div>
  <div class="fcol" style="left:480px"><h4>Company</h4><ul><li>Contact</li><li>About Us</li><li>Client Testimonials</li><li>Project Showcase</li><li>Sitemap</li></ul></div>
  <div class="fcol" style="left:653px"><h4>Services</h4><ul><li>Excavating</li><li>Site Preparation</li><li>Gravel Driveways</li><li>House Pads</li><li>Demolition</li><li>Grading</li><li>Land Clearing</li><li>Bush Hogging</li><li>Storm Clean Up</li><li>Tree and Stump Removal</li><li>Forestry Mulching</li><li>Dump Trailer Services</li></ul></div>
  <div class="fcol" style="left:827px"><h4>Areas Served</h4><ul><li>Pickens County, GA</li><li>Jasper, GA</li><li>Talking Rock, GA</li><li>Nelson, GA</li><li>Marble Hill, GA</li><li>Tate, GA</li><li>Big Canoe, GA</li><li>Ball Ground, GA</li><li>Ellijay, GA</li></ul></div>
  <div class="rule"></div>
  <div class="copy">© 2025 Brindle and Fern LLC. All rights reserved.</div>
</footer>

</body>
</html>
```